Finiding oppertunites in Real Estate 6.15.20

size of ad 7” x 9.6”
1-I like the ad to stand out and attract people's attention.
2-you should be able to see the text of the ad clearly .. see the attachment anything in yellow is instructions.
3-the list of topics should not be the main part of the ad
4-if you decide you want a picture or vector of a person .. (you decide)
then it should be a white male about 25-30 years old wearing a solid white or blue shirt and not long hair.
5-leave 1 inch for footer
see attachment
Good luck

Target Market(s)

potential male students 25-35 years of age

Industry/Entity Type

Education

Requirements
Must have
• will stand out and people would want to see it.
should be able to read the words of ad
Nice to have
• how to make money in real estate on one line

```html
<!DOCTYPE html>
<html lang="en">
<head>
<meta charset="utf-8">
<title>Real Estate Career Course</title>
<link href="https://fonts.googleapis.com/css2?family=Tinos:wght@700&family=Montserrat:wght@500;600;700&family=Arimo:wght@400;700&display=swap" rel="stylesheet">
<style>
  :root {
    --navy: #1f3a8f;
    --navy-deep: #1b2f78;
    --blue: #2048a8;
    --orange: #f26b1d;
    --white: #ffffff;
    --ink: #222222;
    --mist-top: #f4f5f7;
    --mist-mid: #c9ccd2;
  }
  * { margin: 0; padding: 0; box-sizing: border-box; }
  html, body { width: 875px; height: 1200px; overflow: hidden; background: var(--white); }
  .flyer { position: relative; width: 875px; height: 1200px; overflow: hidden; background: var(--white); }
  .decor { position: absolute; inset: 0; }
  .title {
    position: absolute; top: 30px; left: 250px; width: 630px; text-align: center;
    font-family: "Tinos", "Times New Roman", serif; font-weight: 700;
    color: var(--navy); font-size: 70px; line-height: 1; letter-spacing: -1px;
  }
  .subtitle {
    position: absolute; top: 104px; left: 250px; width: 630px; text-align: center;
    font-family: "Montserrat", Arial, sans-serif; font-weight: 500;
    color: var(--navy); font-size: 29px; letter-spacing: 4px;
  }
  .course-facts {
    position: absolute; top: 255px; left: 470px; width: 260px; text-align: center;
    font-family: "Montserrat", Arial, sans-serif; font-weight: 700; font-size: 26px; line-height: 1.2;
    color: var(--white);
  }
  .course-facts .remote { color: #f7a23a; margin-bottom: 18px; }
  .course-facts .rule { height: 2px; background: var(--white); margin: 14px 14px; }
  .headline {
    position: absolute; top: 645px; left: 0; width: 875px; text-align: center;
    font-family: "Tinos", "Times New Roman", serif; font-weight: 700;
    color: var(--navy); font-size: 30px;
  }
  .audience {
    position: absolute; top: 686px; left: 0; width: 875px; text-align: center;
    font-family: "Arimo", Arial, sans-serif; color: var(--navy-deep); font-size: 26px; line-height: 1.2;
  }
  .quote-box {
    position: absolute; top: 769px; left: 122px; width: 637px; height: 102px;
    background: var(--orange); border-radius: 12px;
    display: flex; align-items: center; justify-content: center; text-align: center;
    font-family: "Tinos", "Times New Roman", serif; font-weight: 700;
    color: var(--white); font-size: 35px; line-height: 1.1;
  }
  .topics-label {
    position: absolute; top: 896px; left: 0; width: 875px; text-align: center;
    font-family: "Arimo", Arial, sans-serif; font-weight: 700; font-size: 15px; color: var(--ink);
  }
  .topics {
    position: absolute; top: 930px; left: 115px; display: flex; gap: 0;
    font-family: "Arimo", Arial, sans-serif; font-size: 17px; line-height: 1.3; color: var(--ink);
    list-style: none;
  }
  .topics ul { list-style: none; }
  .topics ul:nth-child(1) { width: 244px; }
  .topics ul:nth-child(2) { width: 252px; }
  .footer {
    position: absolute; left: 0; bottom: 0; width: 875px; height: 127px;
    background: linear-gradient(90deg, var(--navy-deep), var(--blue) 60%, var(--navy-deep));
  }
</style>
</head>
<body>
<main class="flyer">
  <svg class="decor" width="875" height="1200" viewBox="0 0 875 1200">
    <defs>
      <linearGradient id="scene-fade" x1="0" y1="0" x2="0" y2="1">
        <stop offset="0" stop-color="#ffffff"/>
        <stop offset="0.35" stop-color="#e3e5e9"/>
        <stop offset="1" stop-color="#b8bcc4"/>
      </linearGradient>
      <linearGradient id="portrait-tone" x1="0" y1="0" x2="1" y2="1">
        <stop offset="0" stop-color="#6f7a5e"/>
        <stop offset="0.5" stop-color="#3e4350"/>
        <stop offset="1" stop-color="#1f2430"/>
      </linearGradient>
      <linearGradient id="facts-fill" x1="0" y1="0" x2="0" y2="1">
        <stop offset="0" stop-color="#1d3484"/>
        <stop offset="1" stop-color="#2458b3"/>
      </linearGradient>
    </defs>
    <polygon fill="#f26b1d" points="0,0 252,0 252,185 0,480"/>
    <polygon fill="#f26b1d" points="640,225 875,135 875,520 690,520"/>
    <rect role="img" aria-label="Soft photo of suburban homes along a street" x="0" y="620" width="875" height="453" fill="url(#scene-fade)"/>
    <polygon role="img" aria-label="Photo of a smiling young real estate agent in a dark suit holding a clipboard" fill="url(#portrait-tone)" stroke="#ffffff" stroke-width="8"
      points="215,190 415,190 520,395 415,600 215,600 110,395"/>
    <polygon fill="url(#facts-fill)" stroke="#ffffff" stroke-width="8"
      points="515,240 680,240 768,395 680,550 515,550 428,395"/>
  </svg>

  <h1 class="title">REAL ESTATE</h1>
  <p class="subtitle">CAREER COURSE</p>

  <div class="course-facts">
    <p class="remote">REMOTE<br>SESSIONS</p>
    <p>12 SESSION<br>COURSE</p>
    <div class="rule"></div>
    <p>CLASSES<br>STARTING<br>JUNE 16</p>
  </div>

  <h2 class="headline">HOW TO MAKE MONEY IN REAL ESTATE?</h2>
  <p class="audience">For those who have started or<br>would like to go into Real Estate</p>

  <blockquote class="quote-box">“An investment in knowledge<br>opens up untold opportunities”</blockquote>

  <p class="topics-label">A PARTIAL LISTING OF TOPICS:</p>
  <div class="topics">
    <ul>
      <li>Single-family</li>
      <li>Multifamily</li>
      <li>Management</li>
      <li>Real Estate Concepts</li>
      <li>Real Estate law</li>
    </ul>
    <ul>
      <li>Investment properties</li>
      <li>Foreclosures</li>
      <li>Rehab</li>
      <li>Foreclosures</li>
      <li>Short sales</li>
    </ul>
    <ul>
      <li>Development</li>
      <li>Financial modeling</li>
      <li>HUD properties</li>
      <li>Due Diligence</li>
    </ul>
  </div>

  <footer class="footer"></footer>
</main>
</body>
</html>
```